Very basic draft completed. Need someone to apply their creative magic

I am building a new website for my business and looking for a designer to assist me on a part-time basis.

My business is a booking site for classes and lessons. It is essentially a directory service, and needs to conform to a standard web-layout that is easy to navigate and familiar to users (i.e. nothing to creative). The function and structure i have adopted is common amongst sites like quolt, hotel booking services, etc.

The first task on my list is to develop the main page. I have already compiled a draft of the first page using Fireworks (see attached) and am looking for someone to cast their creative magic to this draft while maintaining the general layout of the page. After the main page is developed, I will be looking for the same designer to assist with the rest of the site.

Design wise, I'd like to go for a slightly retro feel
By this I mean a moderately modern page with a spark of retro here and there. If you look at my draft you'll notice that I've used regular font for most text, and retro/old-school fonts for surburb names.

I happy for you to suggest colours, but regular page elements such as web links need to remain standard (i.e links = blue) so that they are familiar and identifiable to my users.

Other points:
1) I don't want the page to be too dark (dark headings, images and borders are fine, but I'd like to maintain white or light backgrounds)

2) Positioning: The Body should be centred, with the Header and Footer extending across the hole screen (as illustrated in my draft)

3) I'm happy if the design includes images from photostock libraries.The Silhoute picture for my draft were choosen because there are hundreds of them, and I can regularly change them on the site - keeping it fresh and new. I'd be very happy if the design incorporate images that could also be place often using photo stock images (i.e. happy to keep silhoutes, but leave it to you to decide what looks best)

Note: I'm happy for you to "copy" art work from any photo stock site, and I will pay for the full quality images when the design is selected.

4) The page Footer needs a lot of attention. It will contain standard Footer links/elements.

5) You are free to do anything to the Header section. It needs to have login/register elements

I'm happy to provide further comments, or review other sites/work to help direct design work.

Hi All,

I've updated the project brief, eliminating many of the requirements and giving you the freedom with design submissions, etc. I've also added the $20 payment for submissions. 
Cheers,
Morwen

Reason: I'm away on holiday and will review your submissions and provide feedback when I get back.

```html
<!DOCTYPE html>
<html lang="en">
<head>
<meta charset="utf-8">
<title>Step Outside – Courses &amp; Activities</title>
<link href="https://fonts.googleapis.com/css2?family=Open+Sans:wght@400;600;700;800&display=swap" rel="stylesheet">
<style>
:root{
  --orange-top:#ffc23a;
  --orange-bottom:#f9a51c;
  --ink:#222;
  --text:#444;
  --muted:#888;
  --link:#1a8fd6;
  --panel:#ededed;
  --panel-border:#c9c9c9;
  --bar:#d4d4d4;
  --accent-blue:#8ec6ea;
  --slider-dot:#2a9fd8;
  --white:#fff;
}
*{box-sizing:border-box;margin:0;padding:0}
html,body{width:925px;height:1200px;overflow:hidden;background:var(--white)}
body{position:relative;font-family:"Open Sans",Arial,sans-serif;color:var(--text);font-size:11px}
a{color:var(--link)}
.abs{position:absolute}

/* header */
.site-header{position:absolute;left:0;top:0;width:925px;height:104px;border-top:5px solid #111;
  background:linear-gradient(var(--orange-top),var(--orange-bottom));border-bottom:1px solid #c98a1a}
.brand{position:absolute;left:36px;top:35px;font-size:31px;font-weight:800;color:#111;letter-spacing:-.5px;line-height:1}
.tagline{position:absolute;left:38px;top:70px;font-size:12.5px;color:#5a3a06;font-weight:400}
.suburb{position:absolute;color:rgba(255,255,255,.35);font-weight:600;white-space:nowrap}
.silhouette{position:absolute;background:rgba(20,20,20,.8)}
.change-location{position:absolute;left:730px;top:80px;font-size:12px;color:#111;text-decoration:underline}

/* panels */
.login{left:25px;top:122px;width:186px;height:105px;background:var(--panel);border:1px solid var(--panel-border)}
.login h2{font-size:13px;font-weight:400;color:var(--ink);position:absolute;left:14px;top:11px}
.field{position:absolute;left:14px;width:150px;height:14px;background:var(--white);border:1px solid #bbb;font-size:10px;color:#777;padding-left:5px;line-height:12px}
.btn-signin{position:absolute;left:114px;top:77px;width:50px;height:17px;background:linear-gradient(#ffc94a,#f6a21a);border:1px solid #d08a14;border-radius:2px;font-size:11px;color:#333;text-align:center;line-height:15px}

.search{left:216px;top:122px;width:682px;height:105px;background:var(--panel);border:1px solid var(--panel-border)}
.search label.title{position:absolute;left:17px;top:25px;font-size:12px;color:var(--ink)}
.search .query{position:absolute;left:15px;top:45px;width:147px;height:16px;background:var(--white);border:1px solid #ccc;font-size:10px;color:#999;padding-left:5px;line-height:14px}
.go{position:absolute;left:144px;top:66px;width:19px;height:15px;background:#111;color:var(--white);font-size:8px;text-align:center;line-height:15px}
.criteria{position:absolute;left:192px;top:5px;font-size:10px;color:var(--text)}
.criteria a{margin-left:4px}
.date-label{position:absolute;top:29px;font-size:11px;color:var(--ink)}
.date{position:absolute;top:29px;width:66px;height:15px;border:1px solid #ccc;background:var(--white);font-size:9px;color:#999;padding-left:3px;line-height:13px}
.day{position:absolute;font-size:11px;color:var(--ink);display:flex;align-items:center;gap:6px}
.box{width:11px;height:11px;border:1px solid #777;background:var(--white);position:relative}
.divider{position:absolute;top:10px;width:1px;height:82px;background:#d6d6d6}
.select{position:absolute;left:443px;top:42px;width:111px;height:16px;border:1px solid #bbb;background:var(--white);font-size:9px;color:#888;padding-left:4px;line-height:14px}
.select span{position:absolute;right:0;top:0;width:13px;height:14px;background:#ccc}
.btn-filter{position:absolute;left:585px;top:40px;width:62px;height:19px;background:linear-gradient(#f4f4f4,#d2d2d2);border:1px solid #aaa;border-radius:2px;font-size:11px;text-align:center;line-height:17px;color:var(--ink)}

.side-head{position:absolute;left:25px;width:186px;height:25px;background:linear-gradient(#fafafa,#e2e2e2);border:1px solid var(--panel-border);font-size:12px;color:var(--ink);padding:4px 11px}
.side-head small{font-size:9px}
.categories{position:absolute;left:38px;top:269px;list-style:none;font-size:12px;color:var(--ink)}
.categories li{height:18px;display:flex;align-items:center;white-space:pre}
.categories .count{color:var(--muted)}
.categories .sub{padding-left:30px;height:18px;color:var(--text)}
.toggle{width:12px;height:12px;border-radius:50%;background:#111;position:relative;margin-right:10px}
.toggle::before{content:"";position:absolute;left:3px;top:5px;width:6px;height:2px;background:var(--white)}
.toggle.plus::after{content:"";position:absolute;left:5px;top:3px;width:2px;height:6px;background:var(--white)}
.refine{position:absolute;left:25px;top:586px;width:186px;height:425px;background:linear-gradient(#e9e9e9,#fff)}
.refine-label{position:absolute;left:11px;font-size:10px;color:var(--ink)}
.refine-label span{color:var(--muted);margin-left:6px}
.slider{position:absolute;left:15px;width:142px;height:3px;background:#999;border-radius:2px;box-shadow:0 1px 0 #fff}
.slider i{position:absolute;top:-3px;width:9px;height:9px;border-radius:50%;background:var(--slider-dot)}
.refine hr{position:absolute;left:0;top:73px;width:186px;border:0;border-top:1px solid #ccc}

/* listing */
.list-head{position:absolute;left:216px;top:233px;width:682px;height:26px;background:var(--bar);font-size:12.5px;color:var(--ink);line-height:26px}
.list-head span{position:absolute}
.list-head .sep{width:1px;height:18px;top:4px;background:#aaa}
.listing{position:absolute;left:216px;top:266px;width:682px}
.course{position:relative;height:100px;margin-bottom:4px;background:linear-gradient(90deg,#fff 0%,#fafafa 45%,#dedede 100%)}
.course.alt{border-right:3px solid var(--accent-blue)}
.thumb{position:absolute;left:8px;top:12px;width:74px;height:70px;border:3px solid var(--white);box-shadow:0 0 2px rgba(0,0,0,.5)}
.course h3{position:absolute;left:90px;top:9px;font-size:11px;font-weight:700;color:var(--link)}
.course .host{position:absolute;left:90px;top:24px;font-size:10px;color:var(--ink)}
.course p{position:absolute;left:90px;top:38px;width:358px;font-size:10px;line-height:13px;color:#666}
.course .more{position:absolute;left:414px;top:64px;font-size:10px;text-decoration:underline}
.schedule{position:absolute;left:485px;top:12px;font-size:8.5px;line-height:11.7px;color:#666}
.schedule b{display:inline-block;width:13px;text-align:center;font-weight:400;color:var(--ink)}
.loc-icon{position:absolute;left:565px;top:11px;width:22px;height:22px;border-radius:4px;background:linear-gradient(#fff1b3,#f3cd6b);box-shadow:0 0 2px rgba(0,0,0,.3)}
.loc-icon svg{position:absolute;left:5px;top:3px}
.loc-name{position:absolute;left:564px;top:40px;font-size:10px;color:var(--muted)}
.price{position:absolute;left:634px;top:22px;font-size:19px;color:#111}
.unit{position:absolute;left:630px;top:50px;width:44px;text-align:center;font-size:10px;line-height:13px;color:var(--muted)}

/* footer */
.site-footer{position:absolute;left:0;top:1012px;width:925px;height:188px;background:linear-gradient(#f4f4f6,#e6e6ec);border-top:1px solid #c8c8d0}
.foot-col{position:absolute;top:22px;font-size:11px;line-height:16px;color:var(--text)}
.foot-col h4{font-size:13px;font-weight:400;color:#111;margin-bottom:8px}
.foot-col strong{font-weight:600;color:var(--ink)}
</style>
</head>
<body>

<header class="site-header">
  <div class="brand">Step Outside</div>
  <div class="tagline">Find a class and learn a new skill this week</div>
  <div class="silhouette" role="img" aria-label="Silhouette of a guitarist" style="left:310px;top:10px;width:32px;height:86px;border-radius:45% 45% 12% 12%"></div>
  <span class="suburb" style="left:460px;top:10px;font-size:15px">TOORAK</span>
  <span class="suburb" style="left:553px;top:6px;font-size:21px">Prahran</span>
  <span class="suburb" style="left:386px;top:30px;font-size:17px">Southbank</span>
  <span class="suburb" style="left:483px;top:42px;font-size:16px">South Melbourne</span>
  <span class="suburb" style="left:628px;top:30px;font-size:17px">Melb.</span>
  <span class="suburb" style="left:688px;top:30px;font-size:17px">City of Kilda</span>
  <span class="suburb" style="left:675px;top:50px;font-size:14px">MIDDLEPARK</span>
  <span class="suburb" style="left:517px;top:60px;font-size:16px">WINDSOR</span>
  <span class="suburb" style="left:611px;top:68px;font-size:13px">Port Melbourne</span>
  <div class="silhouette" role="img" aria-label="Silhouettes of two people playing football" style="left:815px;top:38px;width:95px;height:50px;border-radius:30%"></div>
  <a class="change-location">change location</a>
</header>

<section class="abs login">
  <h2>User Login Here</h2>
  <div class="field" style="top:34px">username</div>
  <div class="field" style="top:55px">***********</div>
  <div class="btn-signin">Sign in</div>
</section>

<section class="abs search">
  <label class="title">Search here</label>
  <div class="query">type course here</div>
  <div class="go">GO</div>
  <div class="criteria">optional search criteria <a>hide</a></div>
  <span class="date-label" style="left:191px">Date from</span>
  <div class="date" style="left:248px">15/12/2011</div>
  <span class="date-label" style="left:322px">to</span>
  <div class="date" style="left:339px">15/12/2011</div>
  <div class="day" style="left:197px;top:59px"><span class="box"></span>Mon</div>
  <div class="day" style="left:197px;top:77px"><span class="box"></span>Tue</div>
  <div class="day" style="left:255px;top:59px"><span class="box"></span>Wed</div>
  <div class="day" style="left:255px;top:77px"><span class="box"></span>Thu</div>
  <div class="day" style="left:308px;top:59px"><span class="box"></span>Fri</div>
  <div class="day" style="left:308px;top:77px"><span class="box"></span>Sat</div>
  <div class="day" style="left:364px;top:57px"><span class="box"></span>Sun</div>
  <div class="day" style="left:364px;top:75px"><span class="box"><svg width="13" height="13" viewBox="0 0 13 13" style="position:absolute;left:-1px;top:-3px"><path d="M2 7l3 3 7-9" fill="none" stroke="#111" stroke-width="2"/></svg></span>All</div>
  <div class="divider" style="left:427px"></div>
  <div class="select">Any Time of Day<span></span></div>
  <div class="divider" style="left:570px"></div>
  <div class="btn-filter">Filter</div>
</section>

<div class="side-head" style="top:233px">Explore Courses &amp; Activities</div>
<ul class="categories">
  <li><i class="toggle plus"></i>Visual Arts <span class="count">(32)</span></li>
  <li><i class="toggle plus"></i>Cooking <span class="count">(14)</span></li>
  <li><i class="toggle plus"></i>Health / Fitness <span class="count">(8)</span></li>
  <li><i class="toggle plus"></i>Home / Life <span class="count">(19)</span></li>
  <li><i class="toggle"></i>Languages <span class="count">(12)</span></li>
  <li class="sub" style="margin-top:2px">Danish <span class="count">(1)</span></li>
  <li class="sub">French <span class="count">(3)</span></li>
  <li class="sub">German <span class="count">(1)</span></li>
  <li class="sub">Mandarin <span class="count">(1)</span></li>
  <li class="sub">Portugese <span class="count">(1)</span></li>
  <li class="sub">Spanish <span class="count">(4)</span></li>
  <li style="margin-top:2px"><i class="toggle plus"></i>Performing Arts <span class="count">(31)</span></li>
  <li><i class="toggle plus"></i>Professional <span class="count">(28)</span></li>
  <li><i class="toggle plus"></i>Tech / Internet <span class="count">(5)</span></li>
  <li><i class="toggle plus"></i>Arts &amp; Sciences <span class="count">(9)</span></li>
</ul>

<div class="refine">
  <span class="refine-label" style="top:26px">Age:<span>18yrs+</span></span>
  <div class="slider" style="top:50px"><i style="left:90px"></i></div>
  <hr>
  <span class="refine-label" style="top:89px">Max Price:<span>$150</span></span>
  <div class="slider" style="top:111px"><i style="left:92px"></i></div>
</div>
<div class="side-head" style="top:561px">Refine search <small>(recommended)</small></div>

<div class="list-head">
  <span style="left:13px">Showing: All Courses &amp; Activities</span>
  <span style="left:474px">Schedule</span>
  <span class="sep" style="left:547px"></span>
  <span style="left:562px">Location</span>
  <span class="sep" style="left:624px"></span>
  <span style="left:637px">Price</span>
</div>

<main class="listing">
  <article class="course">
    <div class="thumb" role="img" aria-label="Couple dancing salsa" style="background:linear-gradient(135deg,#6a2a1e,#c9b7a0 60%,#3b1a14)"></div>
    <h3>Salsa Patterns</h3><div class="host">with Vela Salsa Dance Company</div>
    <p>Brightpath Studio gives you relaxed weekly salsa lessons made for new dancers, so that every student can move with the music and build real confidence on the floor.</p>
    <a class="more">read more</a>
    <div class="schedule"><b>M</b>6pm<br><b>T</b>6pm<br><b>W</b>5pm, 7pm<br><b>T</b>-<br><b>F</b>7pm<br><b>S</b>-<br><b>S</b>-</div>
    <div class="loc-icon"><svg width="12" height="15" viewBox="0 0 12 15"><path d="M6 14C2 9 1 7 1 5a5 5 0 0 1 10 0c0 2-1 4-5 9z" fill="#d9453a"/><circle cx="6" cy="5" r="1.8" fill="#fff"/></svg></div>
    <div class="loc-name">South Bank</div><div class="price">$15</div><div class="unit">single session</div>
  </article>
  <article class="course alt">
    <div class="thumb" role="img" aria-label="Dancer in a lilac gown" style="background:radial-gradient(circle at 50% 60%,#d8c4ef,#3a2a6a 70%)"></div>
    <h3>Salsa Patterns</h3><div class="host">with Vela Salsa Dance Company</div>
    <p>Brightpath Studio gives you relaxed weekly salsa lessons made for new dancers, so that every student can move with the music and build real confidence on the floor.</p>
    <a class="more">read more</a>
    <div class="schedule"><b>M</b>6pm<br><b>T</b>6pm<br><b>W</b>5pm, 7pm<br><b>T</b>-<br><b>F</b>7pm<br><b>S</b>-<br><b>S</b>-</div>
    <div class="loc-icon"><svg width="12" height="15" viewBox="0 0 12 15"><path d="M6 14C2 9 1 7 1 5a5 5 0 0 1 10 0c0 2-1 4-5 9z" fill="#d9453a"/><circle cx="6" cy="5" r="1.8" fill="#fff"/></svg></div>
    <div class="loc-name">South Bank</div><div class="price">$15</div><div class="unit">single session</div>
  </article>
  <article class="course">
    <div class="thumb" role="img" aria-label="Dancer on a dark stage" style="background:linear-gradient(135deg,#1a0c0c,#5a2a28 55%,#120808)"></div>
    <h3>Salsa Patterns</h3><div class="host">with Vela Salsa Dance Company</div>
    <p>Brightpath Studio gives you relaxed weekly salsa lessons made for new dancers, so that every student can move with the music and build real confidence on the floor.</p>
    <a class="more">read more</a>
    <div class="schedule"><b>M</b>6pm<br><b>T</b>6pm<br><b>W</b>5pm, 7pm<br><b>T</b>-<br><b>F</b>7pm<br><b>S</b>-<br><b>S</b>-</div>
    <div class="loc-icon"><svg width="12" height="15" viewBox="0 0 12 15"><path d="M6 14C2 9 1 7 1 5a5 5 0 0 1 10 0c0 2-1 4-5 9z" fill="#d9453a"/><circle cx="6" cy="5" r="1.8" fill="#fff"/></svg></div>
    <div class="loc-name">South Bank</div><div class="price">$15</div><div class="unit">single session</div>
  </article>
  <article class="course alt">
    <div class="thumb" role="img" aria-label="Fitness class stretching in a studio" style="background:linear-gradient(135deg,#d9b77a,#6b4a2c 60%,#c8a870)"></div>
    <h3>Salsa Patterns</h3><div class="host">with Vela Salsa Dance Company</div>
    <p>Brightpath Studio gives you relaxed weekly salsa lessons made for new dancers, so that every student can move with the music and build real confidence on the floor.</p>
    <a class="more">read more</a>
    <div class="schedule"><b>M</b>6pm<br><b>T</b>6pm<br><b>W</b>5pm, 7pm<br><b>T</b>-<br><b>F</b>7pm<br><b>S</b>-<br><b>S</b>-</div>
    <div class="loc-icon"><svg width="12" height="15" viewBox="0 0 12 15"><path d="M6 14C2 9 1 7 1 5a5 5 0 0 1 10 0c0 2-1 4-5 9z" fill="#d9453a"/><circle cx="6" cy="5" r="1.8" fill="#fff"/></svg></div>
    <div class="loc-name">South Bank</div><div class="price">$15</div><div class="unit">single session</div>
  </article>
  <article class="course">
    <div class="thumb" role="img" aria-label="Pilates exercise on a mat" style="background:linear-gradient(135deg,#e6c690,#8a6440 55%,#4a6a8a)"></div>
    <h3>Salsa Patterns</h3><div class="host">with Vela Salsa Dance Company</div>
    <p>Brightpath Studio gives you relaxed weekly salsa lessons made for new dancers, so that every student can move with the music and build real confidence on the floor.</p>
    <a class="more">read more</a>
    <div class="schedule"><b>M</b>6pm<br><b>T</b>6pm<br><b>W</b>5pm, 7pm<br><b>T</b>-<br><b>F</b>7pm<br><b>S</b>-<br><b>S</b>-</div>
    <div class="loc-icon"><svg width="12" height="15" viewBox="0 0 12 15"><path d="M6 14C2 9 1 7 1 5a5 5 0 0 1 10 0c0 2-1 4-5 9z" fill="#d9453a"/><circle cx="6" cy="5" r="1.8" fill="#fff"/></svg></div>
    <div class="loc-name">South Bank</div><div class="price">$15</div><div class="unit">single session</div>
  </article>
  <article class="course alt">
    <div class="thumb" role="img" aria-label="Dancer on a dark stage" style="background:linear-gradient(135deg,#1a0c0c,#5a2a28 55%,#120808)"></div>
    <h3>Salsa Patterns</h3><div class="host">with Vela Salsa Dance Company</div>
    <p>Brightpath Studio gives you relaxed weekly salsa lessons made for new dancers, so that every student can move with the music and build real confidence on the floor.</p>
    <a class="more">read more</a>
    <div class="schedule"><b>M</b>6pm<br><b>T</b>6pm<br><b>W</b>5pm, 7pm<br><b>T</b>-<br><b>F</b>7pm<br><b>S</b>-<br><b>S</b>-</div>
    <div class="loc-icon"><svg width="12" height="15" viewBox="0 0 12 15"><path d="M6 14C2 9 1 7 1 5a5 5 0 0 1 10 0c0 2-1 4-5 9z" fill="#d9453a"/><circle cx="6" cy="5" r="1.8" fill="#fff"/></svg></div>
    <div class="loc-name">South Bank</div><div class="price">$15</div><div class="unit">single session</div>
  </article>
  <article class="course">
    <div class="thumb" role="img" aria-label="Dancer in a lilac gown" style="background:radial-gradient(circle at 50% 60%,#d8c4ef,#3a2a6a 70%)"></div>
    <h3>Salsa Patterns</h3><div class="host">with Vela Salsa Dance Company</div>
    <p>Brightpath Studio gives you relaxed weekly salsa lessons made for new dancers, so that every student can move with the music and build real confidence on the floor.</p>
    <a class="more">read more</a>
    <div class="schedule"><b>M</b>6pm<br><b>T</b>6pm<br><b>W</b>5pm, 7pm<br><b>T</b>-<br><b>F</b>7pm<br><b>S</b>-<br><b>S</b>-</div>
    <div class="loc-icon"><svg width="12" height="15" viewBox="0 0 12 15"><path d="M6 14C2 9 1 7 1 5a5 5 0 0 1 10 0c0 2-1 4-5 9z" fill="#d9453a"/><circle cx="6" cy="5" r="1.8" fill="#fff"/></svg></div>
    <div class="loc-name">South Bank</div><div class="price">$15</div><div class="unit">single session</div>
  </article>
</main>

<footer class="site-footer">
  <div class="foot-col" style="left:26px">
    <h4>Contact Us</h4>
    <strong>Name of the Company</strong><br>
    14 Harbour Lane<br>
    Southbank VIC 3006<br>
    Tele: + 1800 000 123<br>
    email hello@stepoutside.example
  </div>
  <div class="foot-col" style="left:201px;top:20px">
    <h4>Customers</h4>
    Register Now<br>Login<br>Manage Booking
  </div>
  <div class="foot-col" style="left:333px">
    <h4>Businesses</h4>
    Register<br>List a Class or Activity
  </div>
</footer>

</body>
</html>
```